KVR Offerings Bundle Custom Icon (NOT company logo - NO AI!!)

This is a product logo, NOT a company logo. Please do NOT submit redesigned KVR logos, that is NOT the ask

We’re seeking visionary designers to craft a modern, dimensional, and brand-aligned visualization of our KVR Offerings Bundle. This visual will serve as a cornerstone graphic across presentations, proposals, sales enablement, and digital media.

Our aim is to unify our six key solution areas under one elegant ecosystem graphic that clearly showcases our offerings, conveys our premium delivery infrastructure, and communicates the value of integrated reporting.

🧬 Core Design Elements

🌟 Centerpiece
KVR Logo should be centered as the strategic nucleus of the graphic.
The structure should evoke precision, credibility, and strategic alignment—not a “web,” hub-and-spoke, or spider-like shape.

Use subtle three-dimensional design depth—shadows, layering, gradient treatments—but avoid gimmicky or overtly artificial 3D renderings.

🔹 The Six KVR Solutions
Each of the six solutions must be visually represented with:
A custom-designed icon (please avoid AI art as we will require the original design files)
The solution name clearly labeled beneath or beside the icon

Each should be distinct through:

A unique color (drawn from our brand palette or complementary hues — avoid multiple blues, grays, or colors that are too close)

Required Solutions & Icon Inspiration:

Solution Name & Icon Inspiration

1. Native
Article-style layout, webpage block, or target within content

2. Display & Video
Video screen, play button, or motion display split-screen

3. Email
Envelope, digital mail symbol, or dynamic message bubble

4. Share of Voice
Megaphone, volume bars, share graph, or overlapping dialogue icons

5. Disease State Education
Medical textbook, glowing lightbulb with cross, or document with a heartbeat line

6. Conference Coverage
Microphone on podium, camera on tripod, or event badge

📌 Important: These six must appear with both icon and name visible in the final composition. They should feel unified but clearly differentiated from one another.

🛁 Supportive Infrastructure

🟡 Premium Publishers
Should be incorporated around or as a subtle frame to the KVR logo, or just outside the six solutions. The idea here is "deliver our solutions through our premium publishers'. So we'd like to see your ideas on how this can look

🔹 Best-in-Class Reporting
Represents the foundation that applies to all six solutions.
Should anchor or underpin the entire structure—think of it as the data backbone.
Suggested visuals: stylized bar chart base, data arc, blueprint grid, or abstract analytic line across the bottom.

📊 Design Requirements

✅ Must-Haves
Clean, sleek, modern aesthetic appropriate for healthcare + media
NO AI-generated art or surreal rendering
Icons, layering, and vector styles preferred
Brand-aligned typography (modern sans-serif fonts recommended)
Must be easily translatable to print, web, and slides

❌ Avoid
Radial spider-web shapes or hub-and-spoke structures
Flat, lifeless visuals
Multiple shades of the same color family
Ornamental or overly decorative treatments

📂 Deliverables

Final visual in vector format (SVG or AI) and high-res PNG
1-paragraph rationale explaining design choices
Color codes and font references
Original icon files

💡 Inspiration Keywords

“Medical-grade design” • “Connected, but strategic” • “Data-driven clarity” • “Premium ecosystem” • “Healthcare innovation” • “Sales enablement-ready”

Need extra days to review

see task details

```html
<!DOCTYPE html>
<html lang="en">
<head>
<meta charset="utf-8">
<title>KVR Offerings Bundle</title>
<link rel="stylesheet" href="https://fonts.googleapis.com/css2?family=Outfit:wght@500;600;700&display=swap">
<style>
  :root {
    --bg: #FBF6EC;
    --navy: #0D2F5B;
    --frame: #E7E1D3;
    --frame-soft: #F3EEE2;
    --gold: #E8A93A;
    --gold-soft: #F6D27E;
    --gold-text: #B8962E;
    --blue: #2F6FCF;
    --blue-soft: #A9C6EE;
    --blue-mid: #5E97E0;
    --purple: #6B63D9;
    --purple-soft: #C3B8F0;
    --green: #1E9278;
    --green-soft: #96D4BE;
    --coral: #C9604A;
    --coral-soft: #EBA595;
    --chart: #2874C7;
    --chart-light: #4A90DC;
  }
  html, body { margin: 0; padding: 0; overflow: hidden; }
  body { width: 800px; height: 1200px; background: var(--bg); }
  .ecosystem { display: block; width: 800px; height: 1200px; font-family: "Outfit", sans-serif; }
  .heading { fill: var(--navy); font-weight: 600; font-size: 26px; letter-spacing: 3px; text-anchor: middle; }
  .label { fill: var(--navy); font-weight: 500; font-size: 31px; text-anchor: middle;
           stroke: var(--bg); stroke-width: 10px; paint-order: stroke; stroke-linejoin: round; }
  .label-education { fill: var(--gold-text); }
  .nucleus-text { fill: var(--navy); font-weight: 700; font-size: 104px; text-anchor: middle; letter-spacing: 1px; }
  .publisher-frame { fill: none; stroke: var(--frame); stroke-width: 5; }
  .publisher-halo { fill: none; stroke: var(--frame-soft); stroke-width: 18; }
  .lift { filter: url(#lift); }
  .nucleus-lift { filter: url(#nucleusLift); }
</style>
</head>
<body>
<svg class="ecosystem" viewBox="0 0 800 1200" xmlns="http://www.w3.org/2000/svg">
  <defs>
    <filter id="lift" x="-30%" y="-30%" width="160%" height="170%">
      <feDropShadow dx="0" dy="4" stdDeviation="4" flood-color="#0D2F5B" flood-opacity="0.14"/>
    </filter>
    <filter id="nucleusLift" x="-30%" y="-30%" width="160%" height="170%">
      <feDropShadow dx="0" dy="8" stdDeviation="9" flood-color="#B07A18" flood-opacity="0.22"/>
    </filter>
    <linearGradient id="nucleusFill" x1="0" y1="0" x2="0" y2="1">
      <stop offset="0" stop-color="#FFFDF8"/>
      <stop offset="1" stop-color="#F7EEDB"/>
    </linearGradient>
    <linearGradient id="blueFill" x1="0" y1="0" x2="0" y2="1">
      <stop offset="0" stop-color="#BBD3F3"/>
      <stop offset="1" stop-color="#98B9E8"/>
    </linearGradient>
    <linearGradient id="purpleFill" x1="0" y1="0" x2="0" y2="1">
      <stop offset="0" stop-color="#D1C8F5"/>
      <stop offset="1" stop-color="#B3A6EA"/>
    </linearGradient>
    <linearGradient id="greenFill" x1="0" y1="0" x2="0" y2="1">
      <stop offset="0" stop-color="#A9DECB"/>
      <stop offset="1" stop-color="#86CAB1"/>
    </linearGradient>
    <linearGradient id="coralFill" x1="0" y1="0" x2="0" y2="1">
      <stop offset="0" stop-color="#F2B8AA"/>
      <stop offset="1" stop-color="#E5957F"/>
    </linearGradient>
    <linearGradient id="goldFill" x1="0" y1="0" x2="0" y2="1">
      <stop offset="0" stop-color="#F9DE97"/>
      <stop offset="1" stop-color="#F2C766"/>
    </linearGradient>
    <linearGradient id="barFill" x1="0" y1="0" x2="0" y2="1">
      <stop offset="0" stop-color="var(--chart-light)"/>
      <stop offset="1" stop-color="var(--chart)"/>
    </linearGradient>
  </defs>

  <text class="heading" x="396" y="127">PREMIUM PUBLISHERS</text>

  <!-- Premium publishers frame: layered soft band, no spokes -->
  <circle class="publisher-halo" cx="400" cy="508" r="268"/>
  <circle class="publisher-frame" cx="400" cy="508" r="268"/>

  <!-- Nucleus -->
  <g class="nucleus nucleus-lift">
    <rect x="279" y="420" width="242" height="185" rx="24" fill="url(#nucleusFill)" stroke="var(--gold)" stroke-width="6"/>
    <rect x="291" y="432" width="218" height="161" rx="16" fill="none" stroke="#F4DCA8" stroke-width="2"/>
    <text class="nucleus-text" x="400" y="549">KVR</text>
  </g>

  <!-- Native -->
  <g class="solution-native">
    <g class="lift">
      <rect x="121" y="256" width="117" height="107" rx="10" fill="url(#blueFill)" stroke="var(--blue)" stroke-width="5"/>
      <path d="M123.5 278 V266 a8 8 0 0 1 8 -8 h96 a8 8 0 0 1 8 8 V278 Z" fill="var(--blue-mid)"/>
      <line x1="121" y1="278" x2="238" y2="278" stroke="var(--blue)" stroke-width="4"/>
      <circle cx="135" cy="268" r="3" fill="var(--blue)"/>
      <circle cx="146" cy="268" r="3" fill="var(--blue)"/>
      <circle cx="157" cy="268" r="3" fill="var(--blue)"/>
      <rect x="139" y="295" width="33" height="41" rx="3" fill="var(--blue-mid)" stroke="var(--blue)" stroke-width="5"/>
      <g stroke="var(--blue)" stroke-width="5" stroke-linecap="round">
        <line x1="187" y1="299" x2="222" y2="299"/>
        <line x1="187" y1="315" x2="222" y2="315"/>
        <line x1="187" y1="331" x2="222" y2="331"/>
      </g>
    </g>
    <text class="label" x="180" y="413">Native</text>
  </g>

  <!-- Display & Video -->
  <g class="solution-display">
    <g class="lift">
      <rect x="332" y="194" width="137" height="91" rx="10" fill="url(#purpleFill)" stroke="var(--purple)" stroke-width="5"/>
      <path d="M385 222 L385 258 L414 240 Z" fill="var(--purple)" fill-opacity="0.75" stroke="var(--purple)" stroke-width="4" stroke-linejoin="round"/>
      <line x1="400" y1="287" x2="400" y2="302" stroke="var(--purple)" stroke-width="5"/>
      <line x1="374" y1="303" x2="426" y2="303" stroke="var(--purple)" stroke-width="5" stroke-linecap="round"/>
    </g>
    <text class="label" x="402" y="348">Display &amp;</text>
    <text class="label" x="402" y="384">Video</text>
  </g>

  <!-- Email -->
  <g class="solution-email">
    <g class="lift">
      <rect x="562" y="278" width="119" height="85" rx="12" fill="url(#greenFill)" stroke="var(--green)" stroke-width="5"/>
      <polyline points="566,284 621,325 677,284" fill="none" stroke="var(--green)" stroke-width="5" stroke-linejoin="round"/>
    </g>
    <text class="label" x="621" y="413">Email</text>
  </g>

  <!-- Conference Coverage -->
  <g class="solution-conference">
    <g class="lift">
      <line x1="134" y1="501" x2="106" y2="533" stroke="var(--coral)" stroke-width="15" stroke-linecap="round"/>
      <line x1="134" y1="501" x2="106" y2="533" stroke="var(--coral-soft)" stroke-width="7" stroke-linecap="round"/>
      <circle cx="149" cy="484" r="23" fill="url(#coralFill)" stroke="var(--coral)" stroke-width="5"/>
      <line x1="134" y1="536" x2="134" y2="558" stroke="var(--coral)" stroke-width="5"/>
      <path d="M108 572 V566 a8 8 0 0 1 8 -8 h36 a8 8 0 0 1 8 8 V572 Z" fill="url(#coralFill)" stroke="var(--coral)" stroke-width="5" stroke-linejoin="round"/>
    </g>
    <text class="label" x="141" y="619">Conference</text>
    <text class="label" x="141" y="655">Coverage</text>
  </g>

  <!-- Share of Voice -->
  <g class="solution-share">
    <g class="lift" stroke="var(--gold)" stroke-width="5" stroke-linejoin="round" stroke-linecap="round">
      <path d="M620 530 L626 560 a6 6 0 0 0 6 5 h6 a5 5 0 0 0 5 -6 L638 530 Z" fill="url(#goldFill)"/>
      <path d="M604 490 H640 L684 465 V556 L640 532 H604 a12 12 0 0 1 -12 -12 V502 a12 12 0 0 1 12 -12 Z" fill="url(#goldFill)"/>
      <line x1="618" y1="491" x2="618" y2="531"/>
      <path d="M684 496 a15 15 0 0 1 0 30" fill="var(--gold-soft)"/>
      <path d="M705 487 a30 30 0 0 1 0 50" fill="none"/>
    </g>
    <text class="label" x="652" y="617">Share of</text>
    <text class="label" x="652" y="654">Voice</text>
  </g>

  <!-- Disease State Education -->
  <g class="solution-education">
    <g class="lift" stroke="var(--gold)" stroke-width="5" stroke-linejoin="round" stroke-linecap="round">
      <path d="M330 700 H380 a20 20 0 0 1 20 14 a20 20 0 0 1 20 -14 H471 V775 H412 L400 781 L388 775 H330 Z" fill="url(#goldFill)"/>
      <path d="M342 690 H470 V762 H342 Z" fill="#F6DA9C"/>
      <line x1="400" y1="632" x2="400" y2="642"/>
      <line x1="372" y1="642" x2="378" y2="650"/>
      <line x1="428" y1="642" x2="422" y2="650"/>
      <path d="M400 653 a32 32 0 0 1 20 57 V722 H380 V710 a32 32 0 0 1 20 -57 Z" fill="#FBE6B4"/>
      <line x1="383" y1="731" x2="417" y2="731"/>
      <line x1="388" y1="740" x2="412" y2="740"/>
      <line x1="400" y1="672" x2="400" y2="698"/>
      <line x1="387" y1="685" x2="413" y2="685"/>
    </g>
    <text class="label label-education" x="400" y="824">Disease State</text>
    <text class="label label-education" x="400" y="860">Education</text>
  </g>

  <!-- Reporting foundation -->
  <g class="reporting lift">
    <rect x="314" y="933" width="45" height="50" fill="url(#barFill)"/>
    <rect x="381" y="912" width="45" height="71" fill="url(#barFill)"/>
    <rect x="445" y="880" width="44" height="103" fill="url(#barFill)"/>
    <rect x="105" y="979" width="590" height="6" rx="3" fill="var(--chart)"/>
  </g>
  <text class="heading" x="393" y="1045">BEST-IN-CLASS REPORTING</text>
</svg>
</body>
</html>
```